Maple Ridge business card design

Card needs to include the following text/items:
Company Logo
Tobin Marsh
Phone # - 555-318-7642
service@mapleridgelandscaping.example
Lawn & landscape maintenance services

```html
<!DOCTYPE html>
<html lang="en">
<head>
<meta charset="utf-8">
<title>Maple Ridge Landscaping – Business Card</title>
<link rel="stylesheet" href="https://fonts.googleapis.com/css2?family=Marcellus+SC&family=Open+Sans:wght@400&display=swap">
<style>
  :root {
    --forest: #0c4429;
    --ink-green: #114a2c;
    --paper: #f4f4f4;
    --backdrop: #e3e3e3;
    --white: #ffffff;
    --text-dark: #1e1e1e;
    --placeholder: #3d6e45;
    --olive: #7a9a3a;
  }
  * { margin: 0; padding: 0; box-sizing: border-box; }
  html, body { width: 1200px; height: 960px; overflow: hidden; }
  body {
    background: var(--backdrop);
    position: relative;
    font-family: "Open Sans", Arial, sans-serif;
  }
  .card {
    position: absolute;
    top: 175px;
    width: 350px;
    height: 613px;
    overflow: hidden;
    text-align: center;
  }
  .card-front { left: 229px; background: var(--forest); color: var(--white); }
  .card-back { left: 634px; background: var(--paper); color: var(--ink-green); }

  .brand-name {
    font-family: "Marcellus SC", Georgia, serif;
    font-weight: 400;
    line-height: 1;
  }
  .brand-name .brand-main { display: block; font-size: 44px; }
  .brand-name .brand-sub { display: block; font-size: 19px; letter-spacing: 0.42em; margin-top: -4px; padding-left: 0.42em; }

  .card-front .brand-name { position: absolute; top: 64px; left: 0; right: 0; }
  .tagline {
    position: absolute; top: 164px; left: 0; right: 0;
    font-family: "Marcellus SC", Georgia, serif;
    font-size: 21px; line-height: 26px;
  }
  .scene-area {
    position: absolute;
    left: -20px; top: 287px;
    width: 390px; height: 390px;
    border-radius: 50%;
    background: var(--placeholder);
    box-shadow: 0 0 0 8px var(--forest), 0 0 0 14px var(--olive);
  }

  .emblem-disc {
    position: absolute; left: 88px; top: 66px;
    width: 174px; height: 174px;
    border-radius: 50%;
    background: var(--placeholder);
    box-shadow: 0 0 0 3px var(--paper), 0 0 0 6px var(--olive);
    clip-path: inset(-10px -10px 28px -10px);
  }
  .card-back .brand-name { position: absolute; top: 218px; left: 0; right: 0; }
  .card-back .brand-name .brand-sub { color: var(--text-dark); }

  .person-name {
    position: absolute; top: 379px; left: 0; right: 0;
    font-family: "Marcellus SC", Georgia, serif;
    font-size: 31px; line-height: 1;
  }
  .person-role {
    position: absolute; top: 413px; left: 0; right: 0;
    font-size: 13px; color: var(--text-dark);
  }
  .contact-rule { position: absolute; left: 63px; top: 452px; }
  .contact-list {
    position: absolute; top: 487px; left: 0; right: 0;
    list-style: none; font-size: 14px; line-height: 20.5px; color: var(--text-dark);
  }
</style>
</head>
<body>
  <section class="card card-front">
    <h1 class="brand-name"><span class="brand-main">Maple Ridge</span><span class="brand-sub">Landscaping</span></h1>
    <p class="tagline">Lawn &amp; Landscape<br>Maintenance Services</p>
    <div class="scene-area" role="img" aria-label="Illustration of a countryside landscape with trees"></div>
  </section>

  <section class="card card-back">
    <div class="emblem-disc" role="img" aria-label="Company emblem illustration"></div>
    <h2 class="brand-name"><span class="brand-main">Maple Ridge</span><span class="brand-sub">Landscaping</span></h2>
    <p class="person-name">Tobin Marsh</p>
    <p class="person-role">OWNER</p>
    <svg class="contact-rule" width="212" height="22" viewBox="0 0 212 22" aria-hidden="true">
      <g fill="none" stroke="#114a2c" stroke-width="2">
        <line x1="0" y1="11" x2="71" y2="11"/>
        <line x1="141" y1="11" x2="212" y2="11"/>
      </g>
      <g fill="#114a2c">
        <circle cx="82" cy="11" r="10"/>
        <circle cx="110" cy="11" r="10"/>
        <circle cx="138" cy="11" r="10"/>
      </g>
      <path d="M78 6 l3 0 l1 3 l-2 1 q1 3 4 4 l1 -2 l3 1 l0 3 q-7 0 -10 -10z" fill="#fff"/>
      <g fill="none" stroke="#fff" stroke-width="1.4">
        <rect x="104" y="7" width="12" height="8"/>
        <polyline points="104,7 110,12 116,7"/>
        <circle cx="138" cy="11" r="6"/>
        <ellipse cx="138" cy="11" rx="2.6" ry="6"/>
        <line x1="132" y1="11" x2="144" y2="11"/>
      </g>
    </svg>
    <ul class="contact-list">
      <li>555-318-7642</li>
      <li>service@mapleridgelandscaping.example</li>
      <li>www.mapleridgelandscaping.example</li>
    </ul>
  </section>
</body>
</html>
```